Kitchen manufaturer business card/logo design

I am a small kitchen manufacturing company that makes and installs all sorts of cabinetry.

The colours im looking to incorporate in the card are light/baby blue, white and black.

Incorporate 5 stars to show quality workmanship and product.

Looking for a modern classy design.
Updates

Hey guys, New idea. The logo should be made using HK in the most modern way possible as well as the full company name below it. Thanks.

Target Market(s)

Anyone with a home thats looking for a new cabinetry of any sort.

Industry/Entity Type

Business

Contact Information for Business Card

Harbor Kitchens
Tod Villaran
PH 0431 582 904
Email- harborkitchens@mailvane.example
ABN- 73 208 561 339
-Kitchens
-Vanities
-Laundries
-Media Units
-Studies
-Wardrobes
-3D Computer Designs

Requirements
Must have

• The front of the card must only have the company name.
The different types of cabinetry I do must be on the back of the card in point form but instead of using points use stars.
Nice to have
• Just think classy and quality

```html
<!DOCTYPE html>
<html lang="en">
<head>
<meta charset="utf-8">
<title>Harbor Kitchens – Business Card</title>
<link href="https://fonts.googleapis.com/css2?family=Open+Sans:wght@400;600;700&display=swap" rel="stylesheet">
<style>
  :root {
    --baby-blue: #7ecfe7;
    --line-blue: #9fdcee;
    --ink: #1f1f1f;
    --paper: #ffffff;
    --backdrop: #e6e6e6;
    --muted: #2c2c2c;
  }
  html, body {
    margin: 0;
    width: 1200px;
    height: 1200px;
    overflow: hidden;
    background: var(--backdrop);
    font-family: "Open Sans", Arial, sans-serif;
  }
  .card {
    position: absolute;
    left: 250px;
    width: 700px;
    height: 400px;
    overflow: hidden;
    box-shadow: 0 6px 18px rgba(0,0,0,0.12);
  }
  .card--front { top: 150px; background: var(--paper); }
  .card--back  { top: 640px; background: var(--baby-blue); }

  /* front */
  .front__rule-v { position: absolute; left: 520px; top: 0; width: 2px; height: 400px; background: var(--line-blue); }
  .front__rule-h { position: absolute; left: 0; top: 290px; width: 700px; height: 2px; background: var(--line-blue); }
  .front__square { position: absolute; left: 522px; top: 292px; width: 110px; height: 108px; background: var(--baby-blue); }
  .front__name-band {
    position: absolute; left: 40px; top: 150px; width: 460px; height: 56px;
    background: var(--baby-blue);
    display: flex; align-items: center; justify-content: center;
  }
  .front__name {
    font-weight: 700; font-size: 32px; letter-spacing: 1px; color: var(--ink); text-transform: uppercase;
  }

  /* back */
  .back__tab { position: absolute; background: var(--ink); }
  .back__tab--left  { left: 0; top: 70px; width: 40px; height: 52px; }
  .back__tab--right { right: 0; top: 270px; width: 44px; height: 60px; }
  .back__owner { position: absolute; left: 60px; top: 72px; color: var(--ink); }
  .back__owner-name { font-weight: 700; font-size: 22px; margin: 0; }
  .back__abn { font-size: 17px; margin: 2px 0 0; color: var(--muted); letter-spacing: 0.5px; }
  .services {
    position: absolute; left: 40px; top: 160px; width: 370px; height: 78px;
    background: var(--ink); color: var(--paper);
    display: flex; flex-direction: column; justify-content: center;
    padding: 0 10px 0 14px; box-sizing: border-box;
    font-size: 15px; line-height: 26px; white-space: nowrap;
  }
  .services__star { color: var(--baby-blue); }
  .back__rule-v { position: absolute; left: 424px; top: 30px; width: 2px; height: 210px; background: var(--ink); }
  .back__rule-h { position: absolute; left: 400px; top: 76px; width: 300px; height: 2px; background: var(--ink); }
  .back__rule-low { position: absolute; left: 424px; top: 252px; width: 276px; height: 2px; background: var(--ink); }
  .back__name-band {
    position: absolute; left: 446px; top: 112px; width: 212px; height: 34px;
    background: var(--ink); display: flex; align-items: center; justify-content: center;
  }
  .back__name { color: var(--paper); font-weight: 700; font-size: 17px; letter-spacing: 0.5px; text-transform: uppercase; }
  .contact { position: absolute; left: 438px; top: 186px; font-size: 14px; color: var(--ink); white-space: nowrap; }
  .contact__row { display: flex; align-items: center; gap: 6px; height: 24px; }
  .contact__icon { width: 15px; height: 15px; flex: none; }
</style>
</head>
<body>

<section class="card card--front" aria-label="Business card front">
  <div class="front__rule-v"></div>
  <div class="front__rule-h"></div>
  <div class="front__square"></div>
  <div class="front__name-band"><span class="front__name">Harbor Kitchens</span></div>
</section>

<section class="card card--back" aria-label="Business card back">
  <div class="back__tab back__tab--left"></div>
  <div class="back__tab back__tab--right"></div>

  <div class="back__owner">
    <p class="back__owner-name">Tod Villaran</p>
    <p class="back__abn">ABN-73 208 561 339</p>
  </div>

  <div class="services">
    <div><span class="services__star">★</span> Kitchens <span class="services__star">★</span> Vanities <span class="services__star">★</span> Laundries <span class="services__star">★</span> Media Units</div>
    <div><span class="services__star">★</span> Studies <span class="services__star">★</span> Wardrobes <span class="services__star">★</span> 3D Computer Designs</div>
  </div>

  <div class="back__rule-v"></div>
  <div class="back__rule-h"></div>
  <div class="back__rule-low"></div>

  <div class="back__name-band"><span class="back__name">Harbor Kitchens</span></div>

  <div class="contact">
    <div class="contact__row">
      <svg class="contact__icon" viewBox="0 0 16 16" aria-hidden="true">
        <rect x="1" y="3" width="14" height="11" rx="2" fill="#1f1f1f"/>
        <rect x="4" y="1" width="8" height="4" rx="1" fill="#1f1f1f"/>
        <rect x="4" y="7" width="2" height="2" fill="#7ecfe7"/><rect x="7" y="7" width="2" height="2" fill="#7ecfe7"/><rect x="10" y="7" width="2" height="2" fill="#7ecfe7"/>
        <rect x="4" y="10" width="2" height="2" fill="#7ecfe7"/><rect x="7" y="10" width="2" height="2" fill="#7ecfe7"/><rect x="10" y="10" width="2" height="2" fill="#7ecfe7"/>
      </svg>
      <span>0431 582 904</span>
    </div>
    <div class="contact__row">
      <svg class="contact__icon" viewBox="0 0 16 16" aria-hidden="true">
        <rect x="1" y="3" width="14" height="10" fill="#1f1f1f"/>
        <path d="M1 3 L8 9 L15 3" fill="none" stroke="#7ecfe7" stroke-width="1.4"/>
      </svg>
      <span>harborkitchens@mailvane.example</span>
    </div>
  </div>
</section>

</body>
</html>
```